Sydney law firm, Pelbury Solicitors, needs a flyer design!

We need a flyer design for our law firm which has been operating in Sydney for over 35 years. We want to send the flyer out to potential clients and also to existing clients to let them know the range of services that we provide. Our corporate colours are white, red and black and we would like these incorporated somewhat. The final design should be clean, modern and professional.

We would like the design to fit a double sided flyer approx. 210mm high x 100mm wide.

Law Firm

Serif
Sans Serif

eb2026
ffffff

• Details needed on the flyer are:
• Pelbury Solicitors
• 3/82 Tarrow Street, Liverpool, NSW 2170
• (02) 9413 5862
• www.pelburysolicitors-example.com.au
• info@pelburysolicitors-example.com.au
• Our areas of practice include:
• Property Law
• Conveyancing
• Leases
• Criminal Law
• Family Law
• Litigation and Dispute Resolution
• Company Law
• Wills and Estates
• Powers of Attorney and Guardianship
• a picture of scales or a picture of a gavel

```html
<!DOCTYPE html>
<html lang="en">
<head>
<meta charset="utf-8">
<title>Pelbury Solicitors – Flyer</title>
<link href="https://fonts.googleapis.com/css2?family=Noto+Sans:wght@400&display=swap" rel="stylesheet">
<style>
  :root {
    --red: #cf2229;
    --ink: #262626;
    --grey-text: #8a8a8a;
    --grey-line: #b9b9b9;
    --paper: #ffffff;
    --backdrop: #e4e4e4;
  }
  html, body {
    margin: 0;
    padding: 0;
    width: 900px;
    height: 1200px;
    overflow: hidden;
    background: var(--backdrop);
    font-family: "Noto Sans", Arial, sans-serif;
  }
  .canvas {
    position: relative;
    width: 900px;
    height: 1200px;
  }
  .flyer {
    position: absolute;
    top: 180px;
    width: 400px;
    height: 840px;
    background: var(--paper);
    box-shadow: 0 2px 6px rgba(0,0,0,0.18);
    overflow: hidden;
  }
  .flyer--front { left: 40px; }
  .flyer--back { left: 460px; }

  /* frames */
  .frame {
    position: absolute;
    box-sizing: border-box;
  }
  .flyer--front .frame {
    left: 30px; right: 30px; top: 30px; bottom: 28px;
    border: 2px solid var(--red);
  }
  .flyer--back .frame {
    left: 28px; right: 28px; top: 32px; bottom: 14px;
    border: 1px solid var(--grey-line);
  }

  /* wordmark */
  .wordmark {
    position: absolute;
    left: 50%;
    transform: translateX(-50%);
    background: var(--paper);
    color: var(--ink);
    font-weight: 400;
    text-align: center;
    line-height: 1;
    white-space: nowrap;
  }
  .wordmark__name { display: block; }
  .wordmark__tag { display: block; }
  .flyer--front .wordmark { top: 14px; padding: 0 12px; }
  .flyer--front .wordmark__name { font-size: 34px; letter-spacing: 2px; }
  .flyer--front .wordmark__tag { font-size: 11px; letter-spacing: 9px; margin-top: 8px; padding-left: 9px; }
  .flyer--back .wordmark { top: 22px; padding: 0 10px; }
  .flyer--back .wordmark__name { font-size: 24px; letter-spacing: 1.5px; }
  .flyer--back .wordmark__tag { font-size: 8px; letter-spacing: 6px; margin-top: 5px; padding-left: 6px; }

  /* front */
  .front-photo {
    position: absolute;
    left: 0; top: 193px;
    width: 398px; height: 272px;
    background: linear-gradient(100deg, #3a3a3a 0%, #6d6d6d 35%, #b9b9b9 60%, #e6e6e6 85%, #f2f2f2 100%);
  }
  .front-headline {
    position: absolute;
    left: 32px; right: 32px; top: 486px;
    margin: 0;
    text-align: center;
    font-size: 17.5px;
    font-weight: 400;
    line-height: 25px;
    color: var(--ink);
    text-transform: uppercase;
  }
  .front-services {
    position: absolute;
    left: 32px; right: 32px; top: 636px;
    margin: 0;
    text-align: center;
    font-size: 15px;
    color: var(--grey-text);
  }
  .front-emblem {
    position: absolute;
    left: 146px; top: 678px;
    width: 108px; height: 124px;
    border-radius: 50% 50% 46% 46%;
    background: radial-gradient(circle at 50% 45%, #dcdcdc 0%, #e9e9e9 60%, #f6f6f6 100%);
  }

  /* back */
  .about {
    position: absolute;
    left: 40px; right: 40px; top: 86px;
    margin: 0;
    text-align: center;
    font-size: 11.5px;
    line-height: 18px;
    color: var(--red);
  }
  .about p { margin: 0 0 18px; }
  .team-photo {
    position: absolute;
    left: 0; top: 242px;
    width: 400px; height: 140px;
    background: linear-gradient(90deg, #f4f4f4 0%, #cfcfcf 12%, #a8a8a8 30%, #d6d6d6 45%, #b3b3b3 62%, #c9c9c9 78%, #9f9f9f 88%, #ececec 100%);
  }
  .practice {
    position: absolute;
    left: 40px; right: 40px; top: 410px;
    text-align: center;
    color: var(--red);
  }
  .practice__title {
    margin: 0 auto;
    width: 258px;
    font-size: 14px;
    font-weight: 400;
    padding-bottom: 3px;
    border-bottom: 1.5px solid var(--red);
  }
  .practice__list {
    list-style: none;
    margin: 8px 0 0;
    padding: 0;
    font-size: 14.5px;
    line-height: 24.2px;
  }
  .contact {
    position: absolute;
    left: 40px; right: 40px; top: 695px;
    border-top: 1.5px solid var(--grey-line);
    padding-top: 12px;
    text-align: center;
    font-style: normal;
    font-size: 13.5px;
    line-height: 21px;
    color: var(--grey-text);
  }
  .contact span { display: block; }
</style>
</head>
<body>
<div class="canvas">

  <section class="flyer flyer--front">
    <div class="frame"></div>
    <div class="wordmark">
      <span class="wordmark__name">PELBURY</span>
      <span class="wordmark__tag">SOLICITORS</span>
    </div>
    <div class="front-photo" role="img" aria-label="Black and white photo of two people shaking hands"></div>
    <h1 class="front-headline">Established for over 30 years,<br>you can feel confident with<br>our team</h1>
    <p class="front-services">- Property Law - Criminal Law - Family Law -</p>
    <div class="front-emblem" role="img" aria-label="Faint grey figure of Lady Justice holding scales within a laurel wreath"></div>
  </section>

  <section class="flyer flyer--back">
    <div class="frame"></div>
    <div class="wordmark">
      <span class="wordmark__name">PELBURY</span>
      <span class="wordmark__tag">SOLICITORS</span>
    </div>
    <div class="about">
      <p>Pelbury Solicitors is a private law firm based in Liverpool that has been servicing the Sydney area for over 30 years. With a dedicated, professional and friendly team we pride ourselves on delivering an exceptional legal service to our clients.</p>
      <p>Offering a complete legal service at affordable rates, our clients really do come first.</p>
    </div>
    <div class="team-photo" role="img" aria-label="Black and white portraits of smiling legal team members"></div>
    <div class="practice">
      <h2 class="practice__title">OUR AREAS OF PRACTICE INCLUDE</h2>
      <ul class="practice__list">
        <li>PROPERTY LAW</li>
        <li>CONVEYANCING</li>
        <li>LEASES</li>
        <li>CRIMINAL LAW</li>
        <li>FAMILY LAW</li>
        <li>LITIGATION AND DISPUTE RESOLUTION</li>
        <li>COMPANY LAW</li>
        <li>WILLS AND ESTATES</li>
        <li>POWERS OF ATTORNEY AND GUARDIANSHIP</li>
      </ul>
    </div>
    <address class="contact">
      <span>PELBURY SOLICITORS</span>
      <span>3/82 Tarrow Street, Liverpool, NSW 2170</span>
      <span>(02) 9413 5862</span>
      <span>www.pelburysolicitors-example.com.au</span>
      <span>info@pelburysolicitors-example.com.au</span>
    </address>
  </section>

</div>
</body>
</html>
```